Design a App to help people have successful dates!

We require an awesome designer to help us with an App design for a new dating app we are introducing! Our App is intended to help Users build confidence is knowing what questions or ask and answer when going on dates! As you can see from our Project Brief, the intent of the app is to display two types of content to the user 1) Dating Questions, and 2) Dating Tips. We have developed wireframes to help convey what each screen should convey. The intent is to 'inform' and 'educate' the User on what questions to ask, or what questions could be asked of them. Also, we would like to include Banner Ads on the 'Question' and 'Tip' screens, which you can see in the brief.

Target Market(s)

Men and women - aged 18 - 45 who need help identifying dating questions

Industry/Entity Type

Dating App

Font styles to use
Sans Serif

Requirements
Must have
• Please review the PDF brief that we have uploaded. Please make the swipe left and right feature modern (I only included the buttons as a guide only). The ‘Courtship Riddle Ace’ App is intended to be a light-hearted, simple, elegant, fun App, to help Users ask and engage in dating questions. Think of this app as an 'LoveBridgeo' (high quality, educated Users) to help users with identifying questions to ask on dates.
Nice to have
• Please review the PDF brief that we have uploaded.
Should not have
• The App is intended to only include genuine, legitimate, clean and appropriate content. This is not a 'Flimbo' stiyle look-up app.

```html
<!DOCTYPE html>
<html lang="en">
<head>
<meta charset="utf-8">
<title>Courtship Riddle Ace – App Flow</title>
<link rel="stylesheet" href="https://fonts.googleapis.com/css2?family=Open+Sans:wght@400;600;700&display=swap">
<style>
  :root{
    --page:#f6f7fc;
    --blob:#eceef8;
    --ink:#2d3450;
    --screen-bg:#eff1fc;
    --sky:#68a5de;
    --sky-deep:#5c97d2;
    --btn-blue:#619fd9;
    --purple:#7b3fe4;
    --teal:#4fd8c5;
    --heart:#e3121b;
    --flow:#e8050d;
    --muted:#7b84ad;
    --card:#ffffff;
  }
  *{box-sizing:border-box;margin:0;padding:0}
  html,body{width:1200px;height:3299px;overflow:hidden}
  body{background:var(--page);font-family:"Open Sans",sans-serif;color:var(--ink);position:relative}
  .blob{position:absolute;border-radius:50%;background:var(--blob)}
  .page-title{position:absolute;top:164px;left:0;width:1200px;text-align:center;font-size:34px;font-weight:600;letter-spacing:.5px;color:var(--ink)}
  .screen{position:absolute;width:399px;height:862px;border-radius:40px;overflow:hidden;background:var(--screen-bg);box-shadow:0 20px 50px rgba(60,70,120,.12)}
  .screen.light{background:#fff}
  .status{position:absolute;top:12px;left:34px;right:24px;display:flex;justify-content:space-between;align-items:center;font-size:15px;font-weight:600;color:var(--ink)}
  .status.on-photo{color:#fff}
  .status svg{display:block}
  .back{position:absolute;left:22px;width:26px;height:20px}
  .screen-title{position:absolute;left:0;right:0;text-align:center;font-size:20px;font-weight:600;color:var(--ink)}
  .hero-photo{position:absolute;left:0;top:0;width:100%;height:652px;background:linear-gradient(170deg,#7cb3e6 0%,#6a9fd8 45%,#7f86c9 75%,#6a9bd6 100%)}
  .hero-wave{position:absolute;left:0;top:640px;width:100%;height:18px}
  .hero-text{position:absolute;left:35px;top:548px;color:#fff;font-size:24px;font-weight:700;line-height:35px}
  .pill{position:absolute;height:53px;border-radius:27px;color:#fff;font-size:14px;font-weight:700;letter-spacing:.4px;display:flex;align-items:center;justify-content:center}
  .terms{position:absolute;top:778px;left:0;right:0;text-align:center;font-size:14px;color:var(--muted)}
  .collage{position:absolute;left:18px;top:125px;width:382px;height:423px;background:linear-gradient(135deg,#5a86b8 0%,#8a7aa6 40%,#b36b7c 55%,#7390bd 75%,#5c8fc7 100%);clip-path:polygon(4% 2%,62% 2%,62% 10%,100% 10%,100% 55%,92% 55%,92% 100%,42% 100%,42% 72%,0 72%)}
  .q-card{position:absolute;left:30px;top:240px;width:341px;height:286px;background:var(--card);border-radius:20px;display:flex;align-items:center;justify-content:center;text-align:center;padding:0 30px;font-size:26px;line-height:35px;color:var(--ink)}
  .tip-card{position:absolute;left:30px;top:240px;width:341px;height:284px;background:var(--card);border-radius:20px;text-align:center;padding:28px 16px 0}
  .tip-card h3{font-size:20px;font-weight:600;margin-bottom:18px}
  .tip-card p{font-size:16px;line-height:23.5px;color:#444a63}
  .tip-card .more{display:block;margin-top:14px;font-size:14px;color:var(--purple);font-weight:600}
  .controls{position:absolute;left:83px;width:234px;height:62px}
  .ad{position:absolute;left:0;width:100%;height:71px;background:linear-gradient(90deg,#5f5448 0%,#a08662 30%,#3d5a6b 55%,#7b6a52 80%,#2f2f36 100%)}
  .home-bar{position:absolute;bottom:14px;left:128px;width:143px;height:5px;border-radius:3px;background:#111}
  .flow{position:absolute;left:0;top:0;pointer-events:none}
</style>
</head>
<body>
  <div class="blob" style="left:640px;top:-250px;width:700px;height:660px"></div>
  <div class="blob" style="left:-260px;top:650px;width:520px;height:700px"></div>
  <div class="blob" style="left:950px;top:1630px;width:500px;height:560px"></div>

  <h1 class="page-title">COURTSHIP RIDDLE ACE</h1>

  <!-- Welcome -->
  <section class="screen light" style="left:152px;top:336px">
    <div class="hero-photo" role="img" aria-label="Photo of a young woman holding a phone and a red paper heart"></div>
    <svg class="hero-wave" viewBox="0 0 399 18" preserveAspectRatio="none">
      <defs><pattern id="wave1" width="12" height="18" patternUnits="userSpaceOnUse"><path d="M0 12 Q3 6 6 12 T12 12 V18 H0Z" fill="#fff"/></pattern></defs>
      <rect width="399" height="18" fill="url(#wave1)"/>
    </svg>
    <div class="hero-text">Courtship Riddle Ace<br>No awkward silences</div>
    <div class="pill" style="left:23px;top:695px;width:353px;background:var(--btn-blue)">GET STARTED</div>
    <div class="terms">Agree wirh Term and Condition</div>
    <div class="home-bar"></div>
  </section>

  <!-- Menu -->
  <section class="screen light" style="left:661px;top:336px">
    <div class="hero-photo" style="background:var(--sky)"></div>
    <div class="status on-photo"><span>9:41</span>
      <svg width="70" height="12" viewBox="0 0 70 12"><rect x="0" y="8" width="3" height="4" fill="#fff"/><rect x="5" y="6" width="3" height="6" fill="#fff"/><rect x="10" y="3" width="3" height="9" fill="#fff"/><rect x="15" y="0" width="3" height="12" fill="#fff"/><path d="M26 5 Q33 -1 40 5 M29 8 Q33 5 37 8" stroke="#fff" stroke-width="2" fill="none"/><circle cx="33" cy="11" r="1.4" fill="#fff"/><rect x="48" y="2" width="20" height="9" rx="2" fill="#fff"/></svg>
    </div>
    <svg class="back" style="top:62px" viewBox="0 0 26 20"><path d="M24 10H3M10 3 3 10l7 7" stroke="#fff" stroke-width="2.4" fill="none" stroke-linecap="round" stroke-linejoin="round"/></svg>
    <div class="collage" role="img" aria-label="Collage of photos showing couples, friends and dates"></div>
    <svg class="hero-wave" viewBox="0 0 399 18" preserveAspectRatio="none">
      <defs><pattern id="wave2" width="12" height="18" patternUnits="userSpaceOnUse"><path d="M0 12 Q3 6 6 12 T12 12 V18 H0Z" fill="#fff"/></pattern></defs>
      <rect width="399" height="18" fill="url(#wave2)"/>
    </svg>
    <div class="pill" style="left:23px;top:681px;width:353px;background:var(--purple)">DATING QUESTIONS</div>
    <div class="pill" style="left:23px;top:745px;width:353px;background:var(--teal)">DATING TIPS</div>
    <div class="home-bar"></div>
  </section>

  <!-- Question screens -->
  <section class="screen" style="left:152px;top:1278px">
    <div class="status"><span>9:41</span>
      <svg width="70" height="12" viewBox="0 0 70 12"><rect x="0" y="8" width="3" height="4" fill="#222"/><rect x="5" y="6" width="3" height="6" fill="#222"/><rect x="10" y="3" width="3" height="9" fill="#222"/><rect x="15" y="0" width="3" height="12" fill="#222"/><path d="M26 5 Q33 -1 40 5 M29 8 Q33 5 37 8" stroke="#222" stroke-width="2" fill="none"/><circle cx="33" cy="11" r="1.4" fill="#222"/><rect x="48" y="2" width="20" height="9" rx="2" fill="#222"/></svg>
    </div>
    <svg class="back" style="top:62px" viewBox="0 0 26 20"><path d="M24 10H3M10 3 3 10l7 7" stroke="#2d3450" stroke-width="2.4" fill="none" stroke-linecap="round" stroke-linejoin="round"/></svg>
    <div class="screen-title" style="top:64px">Dating Questions</div>
    <div class="q-card">Whats make you laught?</div>
    <svg class="controls" style="top:570px" viewBox="0 0 234 62">
      <circle cx="31" cy="31" r="31" fill="var(--purple)"/><path d="M35 22 26 31l9 9" stroke="#fff" stroke-width="3" fill="none" stroke-linecap="round" stroke-linejoin="round"/>
      <circle cx="117" cy="31" r="31" fill="var(--heart)"/><path d="M117 42 C106 34 105 28 108 24 C111 20 116 22 117 26 C118 22 123 20 126 24 C129 28 128 34 117 42Z" stroke="#fff" stroke-width="2.4" fill="none" stroke-linejoin="round"/>
      <circle cx="203" cy="31" r="31" fill="var(--teal)"/><path d="M199 22 208 31l-9 9" stroke="#fff" stroke-width="3" fill="none" stroke-linecap="round" stroke-linejoin="round"/>
    </svg>
    <div class="ad" style="top:756px" role="img" aria-label="Banner ad for the mobile game Harbor Blast"></div>
    <div class="home-bar"></div>
  </section>

  <section class="screen" style="left:661px;top:1278px">
    <div class="status"><span>9:41</span>
      <svg width="70" height="12" viewBox="0 0 70 12"><rect x="0" y="8" width="3" height="4" fill="#222"/><rect x="5" y="6" width="3" height="6" fill="#222"/><rect x="10" y="3" width="3" height="9" fill="#222"/><rect x="15" y="0" width="3" height="12" fill="#222"/><path d="M26 5 Q33 -1 40 5 M29 8 Q33 5 37 8" stroke="#222" stroke-width="2" fill="none"/><circle cx="33" cy="11" r="1.4" fill="#222"/><rect x="48" y="2" width="20" height="9" rx="2" fill="#222"/></svg>
    </div>
    <svg class="back" style="top:62px" viewBox="0 0 26 20"><path d="M24 10H3M10 3 3 10l7 7" stroke="#2d3450" stroke-width="2.4" fill="none" stroke-linecap="round" stroke-linejoin="round"/></svg>
    <div class="screen-title" style="top:64px">Dating Questions</div>
    <div class="q-card">What does your perfect weeked looks like?</div>
    <svg class="controls" style="top:570px" viewBox="0 0 234 62">
      <circle cx="31" cy="31" r="31" fill="var(--purple)"/><path d="M35 22 26 31l9 9" stroke="#fff" stroke-width="3" fill="none" stroke-linecap="round" stroke-linejoin="round"/>
      <circle cx="117" cy="31" r="31" fill="var(--heart)"/><path d="M117 42 C106 34 105 28 108 24 C111 20 116 22 117 26 C118 22 123 20 126 24 C129 28 128 34 117 42Z" stroke="#fff" stroke-width="2.4" fill="none" stroke-linejoin="round"/>
      <circle cx="203" cy="31" r="31" fill="var(--teal)"/><path d="M199 22 208 31l-9 9" stroke="#fff" stroke-width="3" fill="none" stroke-linecap="round" stroke-linejoin="round"/>
    </svg>
    <div class="ad" style="top:756px" role="img" aria-label="Banner ad for the mobile game Harbor Blast"></div>
    <div class="home-bar"></div>
  </section>

  <!-- Tips screen -->
  <section class="screen" style="left:661px;top:2220px">
    <div class="status"><span>9:41</span>
      <svg width="70" height="12" viewBox="0 0 70 12"><rect x="0" y="8" width="3" height="4" fill="#222"/><rect x="5" y="6" width="3" height="6" fill="#222"/><rect x="10" y="3" width="3" height="9" fill="#222"/><rect x="15" y="0" width="3" height="12" fill="#222"/><path d="M26 5 Q33 -1 40 5 M29 8 Q33 5 37 8" stroke="#222" stroke-width="2" fill="none"/><circle cx="33" cy="11" r="1.4" fill="#222"/><rect x="48" y="2" width="20" height="9" rx="2" fill="#222"/></svg>
    </div>
    <svg class="back" style="top:62px" viewBox="0 0 26 20"><path d="M24 10H3M10 3 3 10l7 7" stroke="#2d3450" stroke-width="2.4" fill="none" stroke-linecap="round" stroke-linejoin="round"/></svg>
    <div class="screen-title" style="top:66px">Dating Tips</div>
    <div class="tip-card">
      <h3>Arrive to the date on time.</h3>
      <p>Don’t be one of those “fashiobly late” people. Your date may feel nervous or anxious wheter you are even coming. Make sure you arrive to meet your date on time.</p>
      <span class="more">see more</span>
    </div>
    <svg class="controls" style="top:570px" viewBox="0 0 234 62">
      <circle cx="31" cy="31" r="31" fill="var(--purple)"/><path d="M35 22 26 31l9 9" stroke="#fff" stroke-width="3" fill="none" stroke-linecap="round" stroke-linejoin="round"/>
      <circle cx="117" cy="31" r="31" fill="var(--heart)"/><path d="M117 42 C106 34 105 28 108 24 C111 20 116 22 117 26 C118 22 123 20 126 24 C129 28 128 34 117 42Z" stroke="#fff" stroke-width="2.4" fill="none" stroke-linejoin="round"/>
      <circle cx="203" cy="31" r="31" fill="var(--teal)"/><path d="M199 22 208 31l-9 9" stroke="#fff" stroke-width="3" fill="none" stroke-linecap="round" stroke-linejoin="round"/>
    </svg>
    <div class="ad" style="top:756px" role="img" aria-label="Banner ad for the mobile game Harbor Blast"></div>
    <div class="home-bar"></div>
  </section>

  <!-- Navigation flow -->
  <svg class="flow" width="1200" height="3299" viewBox="0 0 1200 3299">
    <g stroke="var(--flow)" stroke-width="5" fill="none">
      <path d="M451 1058 H602 V708 H782"/>
      <path d="M990 1041 H1132 V1246 H350 V1405"/>
      <path d="M980 1104 H1109 V2641 H1062"/>
      <path d="M438 1900 V1986 H608 V1704 H700"/>
    </g>
    <g fill="var(--flow)">
      <path d="M810 708 766 686 V730Z"/>
      <path d="M350 1446 328 1402 H372Z"/>
      <path d="M1020 2641 1064 2619 V2663Z"/>
      <path d="M742 1704 696 1682 V1726Z"/>
      <circle cx="451" cy="1058" r="22"/>
      <circle cx="990" cy="1041" r="22"/>
      <circle cx="980" cy="1104" r="22"/>
      <circle cx="438" cy="1900" r="22"/>
    </g>
  </svg>
</body>
</html>
```